Marketplace Lending Diagram

I need a diagram drawn of how our marketplace works that will be part of an article posted by a New York publisher.

The diagrams needs to depict the current state of the market and how our company Borrowix is creating a new market.

Our website is here to give you some more information.
http://www.borrowix-example.com/

There is a video on the website explaining further how this new market works

The attached file needs to be re-drawn using Adobe Illustrator and with a more professional style.

The deliverables need to be an AI file, and PNG file of 300 dpi.

Thanks.

Target Market(s)

Financial community - bankers, hedge fund managers, high net worth individuals

Industry/Entity Type

It Company

Font styles to use
Sans Serif

Requirements
Must have
• 1. Title needs to be "Disintermediating Commercial Mortgage Backed Securitization (CMBS)'
• 2. Change 'Before' and 'After' to 'Current Lending' and 'Marketplace Lending'
• 3. Show the flow from Package to Tranche as the creation of CMBS products. Maybe show an extra dotted arrow with a 'CMBS' label?
• 4. The 'Package' picture look should look like a 3D box to symbolise a pooling of loans.
• 5. Between 'Super Fund' and 'Investors' can this look like three 3D packages instead of money. This symbolise different products being sold to investors.
• 6. Rename 'Super Fund' to 'Mutual Fund'.
• 7. The borrower should symbolise a corporation owning a $10m building. Make the borrower look like a business owner. Need a picture of an office building with the words 'collatoral property'
• See this for an example:
• http://www.quelvane.example.jp/servicer/e/service/cmbs.htm
• 8. 'Super Fund' should be a picture of a little plant growing from gold coins:
• http://www.tormeddi-am.example/faqs/images/fundinvestrimg.gif

```html
<!DOCTYPE html>
<html lang="en">
<head>
<meta charset="utf-8">
<title>Disintermediating CMBS – Marketplace Lending Diagram</title>
<link href="https://fonts.googleapis.com/css2?family=Nunito:wght@400;500;600;700;800&display=swap" rel="stylesheet">
<style>
  :root{
    --bg:#fbefc9;
    --teal:#12877e;
    --teal-light:#5bc0b5;
    --orange:#f26b25;
    --panel:#fdf3d6;
    --skin:#f3c9a4;
    --suit:#1d9a8f;
  }
  html,body{margin:0;padding:0;overflow:hidden}
  body{width:1200px;height:848px;background:var(--bg);font-family:"Nunito",Arial,sans-serif;position:relative}
  .title{position:absolute;left:0;top:8px;width:1170px;margin:0;text-align:center;color:var(--orange);
    font-weight:800;font-size:48px;line-height:61px;letter-spacing:.3px}
  .section-heading{position:absolute;margin:0;color:var(--teal);font-weight:600;font-size:43px;line-height:48px;
    padding-bottom:4px;border-bottom:5px solid var(--orange);white-space:nowrap}
  .section-heading.current{left:53px;top:194px;width:319px}
  .section-heading.marketplace{left:733px;top:194px;width:420px}

  .node{position:absolute;box-sizing:border-box;border:3px solid var(--teal);border-bottom:none;background:var(--panel)}
  .node::after{content:"";position:absolute;left:-3px;right:-3px;bottom:0;height:6px;background:var(--orange)}
  .node-label{height:32px;border-bottom:3px solid var(--teal);color:var(--orange);font-weight:500;font-size:21px;
    line-height:32px;text-align:center;letter-spacing:.3px;white-space:nowrap}
  .node-body{position:absolute;left:0;right:0;top:35px;bottom:6px}
  .node-body svg{position:absolute;left:50%;top:50%;transform:translate(-50%,-50%)}

  .figure{position:absolute}
  .people{background:linear-gradient(180deg,var(--skin) 0 30%,var(--suit) 30% 100%);border-radius:24px 24px 4px 4px}
  .buildings{background:linear-gradient(180deg,#2aa69a,#12877e);border-radius:2px}
  .collateral-tag{position:absolute;background:var(--orange);color:#fff;font-size:15px;line-height:15px;
    text-align:center;padding:3px 4px;width:70px;font-weight:400}
  .plant-coins{background:radial-gradient(circle at 50% 70%,#f2b431 0 30%,#2aa69a 31% 60%,transparent 61%)}
  .product-packages{position:absolute;left:236px;top:584px}

  .arrows{position:absolute;left:0;top:0}
  .flow-label{position:absolute;color:var(--teal);font-size:19px;font-weight:400;background:var(--bg);padding:0 3px}
  .brand{position:absolute;left:996px;top:478px;display:flex;align-items:center;gap:6px;
    color:var(--orange);font-weight:800;font-size:26px;background:var(--bg)}
  .brand-square{width:14px;height:14px;background:var(--orange)}
</style>
</head>
<body>
  <h1 class="title">Disintermediating Commercial<br>Mortgage Backed Securitization<br>(CMBS)</h1>

  <h2 class="section-heading current">Current Lending</h2>
  <h2 class="section-heading marketplace">Marketplace Lending</h2>

  <svg class="arrows" width="1200" height="848" viewBox="0 0 1200 848" aria-hidden="true">
    <defs>
      <marker id="head" markerWidth="10" markerHeight="10" refX="8" refY="5" orient="auto" markerUnits="userSpaceOnUse">
        <path d="M0,0 L10,5 L0,10 z" fill="#f26b25"/>
      </marker>
      <marker id="head-start" markerWidth="10" markerHeight="10" refX="2" refY="5" orient="auto-start-reverse" markerUnits="userSpaceOnUse">
        <path d="M0,0 L10,5 L0,10 z" fill="#f26b25"/>
      </marker>
    </defs>
    <g stroke="#f26b25" stroke-width="2.5" fill="none">
      <line x1="229" y1="408" x2="296" y2="408" marker-end="url(#head)"/>
      <line x1="391" y1="408" x2="459" y2="408" marker-end="url(#head)"/>
      <line x1="567" y1="408" x2="636" y2="408" marker-end="url(#head)"/>
      <polyline points="766,411 830,411 830,579" marker-end="url(#head)"/>
      <line x1="752" y1="656" x2="684" y2="656" marker-end="url(#head)"/>
      <line x1="553" y1="656" x2="479" y2="656" marker-end="url(#head)"/>
      <line x1="296" y1="652" x2="227" y2="652" marker-end="url(#head)"/>
      <polyline points="639,444 584,444 584,578" stroke-dasharray="8 7" marker-end="url(#head)"/>
      <line x1="1057" y1="421" x2="1057" y2="468" marker-start="url(#head-start)" marker-end="url(#head)"/>
      <line x1="1057" y1="530" x2="1057" y2="578" marker-start="url(#head-start)" marker-end="url(#head)"/>
      <path d="M884,452 H935 V440 L962,464 L935,488 V476 H884 Z" stroke-width="3"/>
    </g>
  </svg>
  <span class="flow-label" style="left:545px;top:506px">CMBS</span>
  <span class="flow-label" style="left:479px;top:613px;background:none">CMBS</span>

  <!-- Current lending flow -->
  <div class="node" style="left:53px;top:340px;width:175px;height:138px">
    <div class="node-label">BORROWER</div>
    <div class="node-body">
      <div class="figure people" role="img" aria-label="Business owner in a suit" style="left:10px;top:20px;width:42px;height:76px"></div>
      <div class="figure buildings" role="img" aria-label="Office building used as collateral" style="left:60px;top:14px;width:80px;height:82px"></div>
      <div class="collateral-tag" style="left:94px;top:60px">collateral property</div>
    </div>
  </div>

  <div class="node" style="left:300px;top:340px;width:89px;height:138px">
    <div class="node-label">APPLY</div>
    <div class="node-body">
      <svg width="66" height="42" viewBox="0 0 66 42" aria-hidden="true">
        <g fill="none" stroke="#12877e" stroke-width="3"><rect x="2" y="2" width="62" height="38"/><line x1="2" y1="15" x2="64" y2="15"/><line x1="2" y1="28" x2="64" y2="28"/></g>
      </svg>
    </div>
  </div>

  <div class="node" style="left:463px;top:340px;width:102px;height:138px">
    <div class="node-label">BANK</div>
    <div class="node-body">
      <svg width="74" height="70" viewBox="0 0 74 70" aria-hidden="true">
        <g fill="#12877e"><path d="M37,2 L72,20 H2 Z"/><rect x="4" y="22" width="66" height="5"/>
        <rect x="9" y="30" width="8" height="26"/><rect x="25" y="30" width="8" height="26"/><rect x="41" y="30" width="8" height="26"/><rect x="57" y="30" width="8" height="26"/>
        <rect x="4" y="58" width="66" height="5"/><rect x="0" y="64" width="74" height="5"/></g>
      </svg>
    </div>
  </div>

  <div class="node" style="left:640px;top:338px;width:125px;height:138px">
    <div class="node-label">PACKAGE</div>
    <div class="node-body">
      <svg width="84" height="82" viewBox="0 0 84 82" aria-hidden="true">
        <g fill="none" stroke="#12877e" stroke-width="3" stroke-linejoin="round">
          <path d="M42,2 L82,20 L82,62 L42,80 L2,62 L2,20 Z"/><path d="M2,20 L42,38 L82,20"/><line x1="42" y1="38" x2="42" y2="80"/>
          <path d="M22,11 L62,29 L62,44"/>
        </g>
      </svg>
    </div>
  </div>

  <div class="node" style="left:755px;top:583px;width:151px;height:137px">
    <div class="node-label">SECURITISE</div>
    <div class="node-body">
      <svg width="120" height="60" viewBox="0 0 120 60" aria-hidden="true">
        <g fill="none" stroke="#12877e" stroke-width="3"><rect x="2" y="12" width="108" height="44"/><line x1="2" y1="26" x2="110" y2="26"/><line x1="2" y1="40" x2="110" y2="40"/></g>
        <circle cx="108" cy="12" r="7" fill="none" stroke="#f26b25" stroke-width="3"/><path d="M104,18 L102,28 L108,24 L114,28 L112,18" fill="#f26b25"/>
      </svg>
    </div>
  </div>

  <div class="node" style="left:556px;top:583px;width:123px;height:137px">
    <div class="node-label">TRANCHE</div>
    <div class="node-body">
      <svg width="104" height="94" viewBox="0 0 104 94" aria-hidden="true">
        <g fill="none" stroke="#12877e" stroke-width="3">
          <rect x="38" y="4" width="26" height="20"/><line x1="38" y1="11" x2="64" y2="11"/><line x1="38" y1="17" x2="64" y2="17"/>
          <rect x="2" y="36" width="26" height="20"/><line x1="2" y1="43" x2="28" y2="43"/><line x1="2" y1="49" x2="28" y2="49"/>
          <rect x="38" y="68" width="26" height="20"/><line x1="38" y1="75" x2="64" y2="75"/><line x1="38" y1="81" x2="64" y2="81"/>
        </g>
        <g fill="#f26b25" font-family="Nunito, Arial, sans-serif" font-size="20" font-weight="400">
          <text x="78" y="22">A</text><text x="78" y="54">B</text><text x="78" y="88">C</text>
        </g>
      </svg>
    </div>
  </div>

  <div class="node" style="left:298px;top:583px;width:176px;height:137px">
    <div class="node-label">MUTUAL FUND</div>
    <div class="node-body">
      <div class="figure plant-coins" role="img" aria-label="Hands holding gold coins with a plant growing from them" style="left:30px;top:6px;width:112px;height:86px"></div>
    </div>
  </div>

  <svg class="product-packages" width="56" height="60" viewBox="0 0 56 60" role="img" aria-label="Three product packages sold to investors">
    <defs>
      <g id="package-cube" stroke="#12877e" stroke-width="1.6" stroke-linejoin="round">
        <path d="M11,0 L22,5 L11,10 L0,5 Z" fill="#bfe6e0"/>
        <path d="M0,5 L11,10 L11,22 L0,17 Z" fill="#5bc0b5"/>
        <path d="M22,5 L11,10 L11,22 L22,17 Z" fill="#2aa69a"/>
      </g>
    </defs>
    <use href="#package-cube" x="20" y="2"/>
    <use href="#package-cube" x="30" y="22"/>
    <use href="#package-cube" x="4" y="32"/>
  </svg>

  <div class="node" style="left:48px;top:583px;width:174px;height:137px">
    <div class="node-label">INVESTORS</div>
    <div class="node-body">
      <div class="figure people" role="img" aria-label="Investor" style="left:16px;top:12px;width:42px;height:80px"></div>
      <div class="figure people" role="img" aria-label="Investor" style="left:63px;top:8px;width:42px;height:84px"></div>
      <div class="figure people" role="img" aria-label="Investor" style="left:110px;top:12px;width:42px;height:80px"></div>
    </div>
  </div>

  <!-- Marketplace lending flow -->
  <div class="node" style="left:977px;top:277px;width:176px;height:137px">
    <div class="node-label">BORROWER</div>
    <div class="node-body">
      <div class="figure people" role="img" aria-label="Business owner in a suit" style="left:12px;top:20px;width:42px;height:76px"></div>
      <div class="figure buildings" role="img" aria-label="Office building used as collateral" style="left:62px;top:14px;width:80px;height:82px"></div>
      <div class="collateral-tag" style="left:96px;top:60px">collateral property</div>
    </div>
  </div>

  <div class="brand"><span class="brand-square"></span>Borrowix</div>

  <div class="node" style="left:975px;top:585px;width:175px;height:135px">
    <div class="node-label">INVESTORS</div>
    <div class="node-body">
      <div class="figure people" role="img" aria-label="Investor" style="left:16px;top:12px;width:42px;height:78px"></div>
      <div class="figure people" role="img" aria-label="Investor" style="left:63px;top:8px;width:42px;height:82px"></div>
      <div class="figure people" role="img" aria-label="Investor" style="left:110px;top:12px;width:42px;height:78px"></div>
    </div>
  </div>
</body>
</html>
```